Infographic and content adjustment

For this project, the website content and the templates are already in place. We would need a professional placement of the content into the website, with appropriate and modern icons and/or high Res photos. The website "plovantix.com" provides service to industry or social associations.

We like to see designs on below two templates to be able to compare. A template is already in place on
www.plovantix.com/new

The second template would be:
www.plovantix.com/new2

We would like to receive designs on both templates, so that we can choose the best.

The designer can use the attached power point content, revise the wording if needed and propose a professional design of those contents in the current template. High Res version of the pictures will be provided if necessary.

Target Market(s)

associations, their members,

Industry/Entity Type

Industry

Requirements
Must have
• easy and fast navigation, relevant icons and pictures, short and direct message.

```html
<!DOCTYPE html>
<html lang="en">
<head>
<meta charset="utf-8">
<title>Plovantix</title>
<link href="https://fonts.googleapis.com/css2?family=Roboto+Condensed:wght@300;400;700&family=Roboto:wght@300&display=swap" rel="stylesheet">
<style>
  :root {
    --nav-bg: #2c3949;
    --nav-line: #1e2834;
    --nav-text: #ffffff;
    --hero-bg: #08a0e6;
    --band-bg: #16a9ea;
    --button-top: #3a8fc6;
    --button-bottom: #1f6ea5;
    --button-border: #14598a;
    --info-top: #0a76aa;
    --info-bottom: #04385c;
    --accent-green: #2ff0a2;
    --heading-dark: #0d1c2b;
    --white: #ffffff;
    --shot-bg: #f3f4f5;
    --shot-bar: #2a2a2a;
  }
  * { margin: 0; padding: 0; box-sizing: border-box; }
  html, body { width: 1200px; height: 872px; overflow: hidden; }
  body { position: relative; font-family: "Roboto Condensed", Arial, sans-serif; background: var(--info-bottom); }

  .site-nav {
    position: absolute; left: 0; top: 0; width: 1200px; height: 52px;
    background: var(--nav-bg); color: var(--nav-text);
  }
  .nav-divider { position: absolute; top: 0; width: 1px; height: 52px; background: var(--nav-line); }
  .menu-icon { position: absolute; left: 38px; top: 18px; }
  .brand-name {
    position: absolute; left: 91px; top: 10px; font-size: 27px; font-weight: 300; letter-spacing: 0.3px;
  }
  .nav-arrow { position: absolute; top: 17px; }
  .nav-link { position: absolute; top: 17px; font-size: 14px; font-weight: 300; }

  .hero {
    position: absolute; left: 0; top: 52px; width: 1200px; height: 293px;
    background: var(--hero-bg); text-align: center;
  }
  .hero-title {
    position: absolute; left: 0; top: 48px; width: 100%;
    font-size: 46px; font-weight: 700; color: var(--white);
  }
  .hero-headline {
    position: absolute; left: 0; top: 120px; width: 100%;
    font-family: "Roboto", Arial, sans-serif; font-weight: 300; font-size: 37px; color: var(--heading-dark);
  }
  .hero-tagline {
    position: absolute; left: 0; top: 170px; width: 100%;
    font-family: "Roboto", Arial, sans-serif; font-weight: 300; font-size: 21px; color: var(--white);
  }

  .cta-band {
    position: absolute; left: 0; top: 345px; width: 1200px; height: 70px; background: var(--band-bg);
  }
  .cta-button {
    position: absolute; left: 478px; top: 11px; width: 247px; height: 50px;
    background: linear-gradient(var(--button-top), var(--button-bottom));
    border: 1px solid var(--button-border);
    color: var(--white); font-size: 25px; font-weight: 300; text-align: center; line-height: 48px;
  }

  .info {
    position: absolute; left: 0; top: 415px; width: 1200px; height: 457px;
    background: linear-gradient(var(--info-top), var(--info-bottom));
    text-align: center;
  }
  .info-title {
    position: absolute; left: 0; top: 25px; width: 100%;
    font-family: "Roboto", Arial, sans-serif; font-weight: 300; font-size: 37px; color: var(--accent-green);
  }
  .info-text {
    position: absolute; left: 205px; top: 82px; width: 790px;
    font-size: 21px; font-weight: 300; line-height: 23px; color: var(--white);
  }
  .screenshot {
    position: absolute; top: 218px; width: 262px; height: 199px;
    background: linear-gradient(var(--shot-bar) 0 10px, var(--shot-bg) 10px);
  }
  .screenshot-tree { left: 282px; }
  .screenshot-wheel { left: 661px; }
</style>
</head>
<body>
  <header class="site-nav">
    <svg class="menu-icon" width="22" height="14" viewBox="0 0 22 14" aria-hidden="true">
      <rect y="0" width="22" height="2" fill="#fff"/><rect y="6" width="22" height="2" fill="#fff"/><rect y="12" width="22" height="2" fill="#fff"/>
    </svg>
    <span class="nav-divider" style="left:74px"></span>
    <span class="brand-name">PLOVANTIX</span>
    <span class="nav-divider" style="left:225px"></span>
    <svg class="nav-arrow" style="left:565px" width="16" height="12" viewBox="0 0 16 12" aria-hidden="true"><path d="M2 10 L8 3 L14 10" stroke="#fff" stroke-width="3" fill="none"/></svg>
    <span class="nav-divider" style="left:602px"></span>
    <svg class="nav-arrow" style="left:623px" width="16" height="12" viewBox="0 0 16 12" aria-hidden="true"><path d="M2 2 L8 9 L14 2" stroke="#fff" stroke-width="3" fill="none"/></svg>
    <span class="nav-divider" style="left:998px"></span>
    <span class="nav-link" style="left:1026px">LOGIN</span>
    <span class="nav-divider" style="left:1097px"></span>
    <span class="nav-link" style="left:1120px">SIGN UP</span>
  </header>

  <section class="hero">
    <h1 class="hero-title">PLOVANTIX</h1>
    <h2 class="hero-headline">DISCOVER POWER OF ECOSYSTEM INTELLIGENCE</h2>
    <p class="hero-tagline">Learn what your network members do .Visualize their impact. Accelerate Their Growth.</p>
  </section>

  <div class="cta-band">
    <div class="cta-button">SHOW ME HOW</div>
  </div>

  <section class="info">
    <h2 class="info-title">WHAT IS PLOVANTIX</h2>
    <p class="info-text">An interactive web-based tool designed to help industry associations succeed. Plovantix will expand your member base by 1) increasing the value you provide to current and potential members and 2) improving your ability to reach them.</p>
    <div class="screenshot screenshot-tree" role="img" aria-label="App screenshot: member profile with a branching tree of capabilities and partner companies"></div>
    <div class="screenshot screenshot-wheel" role="img" aria-label="App screenshot: circular network diagram linking member companies to capability categories"></div>
  </section>
</body>
</html>
```